First Aid Training business needs business card design

We would like a double sided business card designed for a first aid training business - Banksia First Aid. We provide first aid training and , WHS (work, health and safety) training.

The attached word document contains the key information we would like on each side of the business card.

Final design needs to be delivered in print ready format, along with the original file.

```html
<!DOCTYPE html>
<html lang="en">
<head>
<meta charset="utf-8">
<title>Banksia First Aid – Business Card</title>
<link rel="stylesheet" href="https://fonts.googleapis.com/css2?family=Montserrat:wght@600&family=Source+Sans+3:wght@400;700&display=swap">
<style>
  :root {
    --red: #ee2326;
    --grey: #848484;
    --ink: #262223;
    --paper: #ffffff;
    --stage: #ffffff;
  }
  * { box-sizing: border-box; margin: 0; padding: 0; }
  html, body { width: 1200px; height: 900px; overflow: hidden; background: var(--stage); }
  body { position: relative; font-family: "Source Sans 3", sans-serif; color: var(--ink); }

  .card {
    position: absolute; left: 262px; width: 675px; height: 405px;
    background: var(--paper);
    box-shadow: -6px 8px 14px rgba(0,0,0,0.28);
  }
  .card--front { top: 28px; }
  .card--back { top: 467px; }

  .colour-blocks { position: absolute; left: 338px; width: 312px; height: 60px; display: flex; }
  .colour-blocks--top { top: 0; }
  .colour-blocks--bottom { bottom: 0; }
  .colour-blocks span { flex: 1; }
  .red { background: var(--red); }
  .grey { background: var(--grey); }
  .ink { background: var(--ink); }

  .benefits { position: absolute; left: 56px; top: 161px; width: 273px; list-style: none; }
  .benefits li {
    height: 31px; margin-bottom: 7.5px; border-radius: 5px;
    background: var(--red); color: #fff;
    font-size: 15.5px; line-height: 31px; text-align: center; white-space: nowrap;
  }

  .brand { position: absolute; display: flex; align-items: center; font-family: "Montserrat", sans-serif; font-weight: 600; color: var(--ink); }
  .brand__dot { border-radius: 50%; background: var(--red); flex: none; }
  .brand__name { line-height: 1; }
  .brand__name b { display: block; font-weight: 600; }

  .card--front .brand { left: 351px; top: 158px; }
  .card--front .brand__dot { width: 78px; height: 78px; margin-right: 22px; }
  .card--front .brand__main { font-size: 31px; letter-spacing: 0.5px; }
  .card--front .brand__sub { font-size: 14.6px; margin-top: 6px; }

  .tagline { position: absolute; left: 349px; top: 246px; font-weight: 700; font-size: 13.4px; letter-spacing: 0.1px; white-space: nowrap; }

  .holder { position: absolute; right: 348px; top: 118px; display: flex; align-items: center; gap: 13px; }
  .holder__name { font-weight: 700; font-size: 23px; letter-spacing: 0.3px; }
  .holder svg { width: 28px; height: 34px; }

  .name-rule { position: absolute; left: 0; top: 168px; width: 326px; height: 6px; display: flex; }
  .name-rule span { flex: 1; }

  .contacts { position: absolute; right: 349px; top: 193px; list-style: none; }
  .contacts li { display: flex; align-items: center; justify-content: flex-end; gap: 10px; height: 31px; margin-bottom: 6.5px; font-size: 16.5px; letter-spacing: 0.3px; }
  .contacts .icon { width: 28px; height: 31px; border-radius: 5px; background: var(--red); display: flex; align-items: center; justify-content: center; }
  .contacts .icon svg { width: 17px; height: 17px; }

  .card--back .brand { left: 385px; top: 98px; flex-direction: column; text-align: center; width: 222px; }
  .card--back .brand__dot { width: 118px; height: 118px; margin-bottom: 24px; }
  .card--back .brand__main { font-size: 38px; letter-spacing: 0.5px; }
  .card--back .brand__sub { font-size: 18.5px; margin-top: 6px; white-space: nowrap; }
</style>
</head>
<body>

<section class="card card--front" aria-label="Business card front">
  <div class="colour-blocks colour-blocks--top"><span class="red"></span><span class="grey"></span><span class="ink"></span></div>

  <ul class="benefits">
    <li>TIME EFFICIENT</li>
    <li>COST EFFECTIVE</li>
    <li>MINIMISE DOWNTIME FOR YOUR TEAM</li>
  </ul>

  <div class="brand">
    <span class="brand__dot"></span>
    <span class="brand__name"><b class="brand__main">BANKSIA</b><b class="brand__sub">FIRST AID TRAINING</b></span>
  </div>
  <p class="tagline">ONSITE TRAINING – WE CAN COME TO YOU</p>

  <div class="colour-blocks colour-blocks--bottom"><span class="red"></span><span class="grey"></span><span class="ink"></span></div>
</section>

<section class="card card--back" aria-label="Business card back">
  <div class="holder">
    <span class="holder__name">LIAM HARTLEY</span>
    <svg viewBox="0 0 28 34" aria-hidden="true">
      <circle cx="14" cy="9" r="8" fill="#ee2326"/>
      <path d="M0 34 V27 Q0 19 8 19 H20 Q28 19 28 27 V34 Z" fill="#ee2326"/>
    </svg>
  </div>

  <div class="name-rule"><span class="ink"></span><span class="grey"></span><span class="red"></span></div>

  <ul class="contacts">
    <li><span>0400 316 582</span>
      <span class="icon"><svg viewBox="0 0 24 24" aria-hidden="true"><path fill="#fff" d="M6.6 10.8a15.1 15.1 0 0 0 6.6 6.6l2.2-2.2c.3-.3.7-.4 1-.2 1.1.4 2.3.6 3.6.6.6 0 1 .4 1 1V20c0 .6-.4 1-1 1A17 17 0 0 1 3 4c0-.6.4-1 1-1h3.5c.6 0 1 .4 1 1 0 1.3.2 2.5.6 3.6.1.3 0 .7-.2 1z"/></svg></span></li>
    <li><span>help@banksiafirstaid.com.au</span>
      <span class="icon"><svg viewBox="0 0 24 24" aria-hidden="true"><rect x="3" y="5.5" width="18" height="13" fill="none" stroke="#fff" stroke-width="1.6"/><path d="M3 5.5l9 7 9-7M3 18.5l7-6M21 18.5l-7-6" fill="none" stroke="#fff" stroke-width="1.4"/></svg></span></li>
    <li><span>www.banksiafirstaid.com.au</span>
      <span class="icon"><svg viewBox="0 0 24 24" aria-hidden="true"><path fill="#fff" d="M12 2a7 7 0 0 0-7 7c0 5.2 7 13 7 13s7-7.8 7-13a7 7 0 0 0-7-7zm0 9.5A2.5 2.5 0 1 1 12 6.5a2.5 2.5 0 0 1 0 5z"/></svg></span></li>
  </ul>

  <div class="brand">
    <span class="brand__dot"></span>
    <span class="brand__name"><b class="brand__main">BANKSIA</b><b class="brand__sub">FIRST AID TRAINING</b></span>
  </div>
</section>

</body>
</html>
```